Wordpress Design Project (Brookmere)

We need a wordpress design for an established auction and real estate company based in New Hampshire. The winning design will incorporate the colors of logo (red and blue) creatively with black or gray in a very professional and clean layout. Client mentions liking the site http://www.tarvellauction.com/ as a general idea.

Industry/Entity Type

Real Estate

Requirements
Must have
• Navigation:
1) Home (lorem text)
2) Upcoming Auctions
3) Auction Results
4) Sell or Consign
5) About Us
6) Services
7) FAQ
8) Contact Us

Site will have slideshow, initial image attached.
Sidebar widgets:
- Email sign up form
- Featured Auction (like at http://www.pinderauctionco.com) - - - - Video Widget
- Testimonials widget

Footer will have smaller logo, contact info, and 2 association logos (attached)
-
Nice to have
• use of drop-down menu design for 'Services'
1) Appraisals
2) Consulting
Should not have
• please use no gavels in the design

```html
<!DOCTYPE html>
<html lang="en">
<head>
<meta charset="utf-8">
<title>Brookmere Auctions</title>
<link href="https://fonts.googleapis.com/css2?family=Arimo:wght@400;700&display=swap" rel="stylesheet">
<style>
:root{
  --navy:#0c1a55;
  --navy-dark:#08123d;
  --red:#b3191c;
  --red-bright:#d8211f;
  --ink:#222;
  --muted:#555;
  --panel:#1e1e1e;
  --footer:#1b1b1b;
  --line:#d9d9d9;
  --card:#efefef;
}
*{box-sizing:border-box;margin:0;padding:0}
html,body{width:1011px;height:1200px;overflow:hidden}
body{font-family:"Arimo",Arial,sans-serif;background:#e9e9e9;color:var(--ink);position:relative}
.page{position:absolute;left:86px;top:0;width:839px;height:1109px;background:#fff;box-shadow:0 0 4px rgba(0,0,0,.25)}
.abs{position:absolute}
.brand{left:97px;top:30px;display:flex;align-items:center;gap:10px}
.brand-dot{width:44px;height:44px;border-radius:50%;background:var(--navy)}
.brand-name{font-size:28px;color:var(--navy);letter-spacing:1px}
.phone{left:674px;top:48px;font-size:21px;color:#111;letter-spacing:.5px}
.phone span{font-size:14px;color:var(--navy)}
.nav{left:91px;top:107px;width:829px;height:37px;background:var(--navy);display:flex}
.nav a{color:#fff;text-decoration:none;font-size:12.5px;display:flex;align-items:center;justify-content:center;border-right:1px solid #2c3a78;height:100%}
.nav a.active{background:var(--red)}
.dropdown{left:573px;top:145px;width:131px;height:58px;background:var(--red);padding:5px 6px}
.dropdown a{display:block;color:#fff;font-size:12px;text-decoration:none;height:22px;line-height:22px;padding-left:16px;position:relative;margin-bottom:5px;border-radius:3px}
.dropdown a::before{content:"";position:absolute;left:7px;top:8px;border-left:4px solid #fff;border-top:3px solid transparent;border-bottom:3px solid transparent}
.dropdown a.hover{background:var(--navy)}
.hero{left:91px;top:145px;width:587px;height:289px;background:linear-gradient(135deg,#6e5a4e,#b8a89a 40%,#8a7768 70%,#3b302a)}
.featured{left:678px;top:145px;width:242px;height:289px;background:var(--panel);color:#fff;text-align:center}
.featured h2{font-weight:400;font-size:20px;margin-top:16px;padding-left:16px}
.featured .cat{color:var(--red-bright);font-size:10px;font-weight:700;margin-top:10px;line-height:14px;letter-spacing:.3px}
.featured .shot{margin:6px auto 0;width:147px;height:102px;border:3px solid #fff;background:linear-gradient(#8aa6c8,#c9cfd6 55%,#5b5b5b)}
.featured .meta{font-size:10.5px;line-height:14.5px;margin-top:22px}
h1.section{left:100px;top:469px;font-size:17.5px;font-weight:700;color:#333;letter-spacing:.3px}
.card{left:94px;width:573px;height:268px;border:1px solid var(--line);border-radius:4px;background:linear-gradient(#fff,var(--card))}
.card-bar{left:6px;top:5px;width:561px;height:35px;border-radius:5px;background:linear-gradient(#3d3d3d,#111);color:#fff;font-weight:700;font-size:12.5px;line-height:35px;padding-left:15px;letter-spacing:.3px}
.thumb-box{left:11px;top:56px;width:135px;height:144px;background:#fff;border:1px solid var(--line);border-radius:3px}
.thumb{left:10px;top:8px;width:115px;height:80px;background:linear-gradient(90deg,#1a1608,#5a4a1e 50%,#1a1608)}
.details{left:6px;top:102px;width:108px;height:28px;border-radius:4px;background:linear-gradient(var(--red-bright),#a5100f);color:#fff;font-weight:700;font-size:14px;display:flex;align-items:center;gap:10px;padding-left:12px}
.info{left:156px;width:409px;height:95px;background:#fff;border:1px solid var(--line);border-radius:4px;padding:4px 9px;font-size:11px;line-height:13px}
.info .title{color:var(--navy);font-weight:700;font-size:12px;line-height:15px;letter-spacing:.3px;margin-bottom:5px}
.info .lbl{color:var(--red);font-weight:700;font-size:12px}
.info p{margin-bottom:3px}
.video{left:676px;top:462px;width:241px;height:176px;background:linear-gradient(90deg,#3a2a24,#7b6a50 35%,#9c7a4a 50%,#6b2120 75%,#3d2b28)}
.vbar{left:676px;top:618px;width:241px;height:20px;background:#111;color:#fff;font-size:9px;font-weight:700}
.signup{left:676px;top:661px;width:244px;height:194px;background:var(--navy);border:1px solid #000;padding:12px 23px}
.signup h2{color:#fff;font-weight:400;font-size:20px;margin-bottom:17px}
.signup .field{width:196px;height:29px;background:#fff;font-size:10px;color:#999;padding:9px;margin-bottom:15px}
.subscribe{position:absolute;right:23px;top:145px;width:101px;height:29px;background:linear-gradient(var(--red-bright),#a5100f);border-radius:3px;color:#fff;font-weight:700;font-size:14px;text-align:center;line-height:29px;letter-spacing:.5px}
.testi{left:678px;top:880px;width:240px;height:191px;border:1px solid var(--line);background:linear-gradient(#fff,#ececec);padding:12px 16px 12px 20px}
.testi h2{font-weight:400;font-size:17px;margin-bottom:8px;padding-left:1px}
.testi p{font-size:11px;line-height:17px;color:#333;padding:0 4px 0 4px}
.q{font-family:Georgia,serif;color:#999;font-size:22px;line-height:0}
.testi .by{text-align:right;color:var(--red);font-weight:700;font-style:italic;font-size:10.5px;margin-top:10px}
.footer{left:0;top:1109px;width:1011px;height:91px;background:var(--footer);color:#eee;font-size:10.5px}
.footer .contact{position:absolute;left:90px;top:24px;line-height:19px}
.footer .flogo{position:absolute;left:556px;top:22px;width:122px;height:42px;border:1px solid #333;display:flex;align-items:center;gap:5px;padding-left:6px;font-size:14px;color:#fff}
.footer .flogo i{width:20px;height:20px;border-radius:50%;background:#fff;display:block}
.badge1{position:absolute;left:699px;top:22px;width:42px;height:42px;background:#bbb}
.badge2{position:absolute;left:773px;top:22px;width:144px;height:36px;background:#fff}
</style>
</head>
<body>
<div class="page"></div>

<div class="abs brand"><div class="brand-dot"></div><div class="brand-name">BROOKMERE</div></div>
<div class="abs phone"><span>Call us: </span>(800) 555-0142</div>

<nav class="abs nav">
  <a style="width:72px">Home</a>
  <a style="width:151px">Upcoming Auctions</a>
  <a style="width:131px">Auction Results</a>
  <a style="width:129px">Sell or Consign</a>
  <a class="active" style="width:89px">Services</a>
  <a style="width:89px">About Us</a>
  <a style="width:63px">FAQ</a>
  <a style="width:105px;border-right:0">Contact Us</a>
</nav>

<div class="abs hero" role="img" aria-label="Trays of silver coins in protective sleeves"></div>
<div class="abs dropdown"><a class="hover">Appraisals</a><a>Consulting</a></div>

<aside class="abs featured">
  <h2>Featured Auctions</h2>
  <div class="cat">AUTOMOBILES - MULTI LOT<br>AUTO AUCTIONS</div>
  <div class="shot" role="img" aria-label="Silver minivan parked outdoors"></div>
  <div class="meta">07/10/13 at 12:00 PM EDT<br>P.O. Box 40517<br>Keene, NH 03431</div>
</aside>

<h1 class="abs section">Upcoming Auctions</h1>

<article class="abs card" style="top:514px">
  <div class="abs card-bar">HOLLINS WELLNESS CENTER IN DUNMORE, NH</div>
  <div class="abs thumb-box">
    <div class="abs thumb" role="img" aria-label="Photo of two gold coins on a black background"></div>
    <div class="abs details"><svg width="20" height="20" viewBox="0 0 20 20"><rect x="1" y="1" width="18" height="18" rx="3" fill="#fff"/><circle cx="9" cy="9" r="4.5" fill="none" stroke="#b3191c" stroke-width="2"/><line x1="12" y1="12" x2="16" y2="16" stroke="#b3191c" stroke-width="2.5"/></svg>Details</div>
  </div>
  <div class="abs info" style="top:57px">
    <div class="title">Marlow Crane Auctions, LLC NHL 4821 - Everything sold to the high bidder</div>
    Location:<br>Location 1 - 412 Orchard Hill Rd<br>Location 2 - 58 Millbrook Ct # 3<br>Dunmore, NH 03201
  </div>
  <div class="abs info" style="top:158px">
    <p class="lbl">Location:</p>
    <p><b>Began:</b>&nbsp; Friday, May 24, 2013 at 10:06 AM EDT</p>
    <p><b>Ends:</b>&nbsp; Wednesday, June 05, 2013 at 10:00 AM EDT</p>
    2270 Ashford Ln. NE<br>Concord, NH 03301
  </div>
</article>

<article class="abs card" style="top:803px">
  <div class="abs card-bar">HOLLINS WELLNESS CENTER IN DUNMORE, NH</div>
  <div class="abs thumb-box">
    <div class="abs thumb" role="img" aria-label="Photo of two gold coins on a black background"></div>
    <div class="abs details"><svg width="20" height="20" viewBox="0 0 20 20"><rect x="1" y="1" width="18" height="18" rx="3" fill="#fff"/><circle cx="9" cy="9" r="4.5" fill="none" stroke="#b3191c" stroke-width="2"/><line x1="12" y1="12" x2="16" y2="16" stroke="#b3191c" stroke-width="2.5"/></svg>Details</div>
  </div>
  <div class="abs info" style="top:57px">
    <div class="title">Marlow Crane Auctions, LLC NHL 4821 - Everything sold to the high bidder</div>
    Location:<br>Location 1 - 412 Orchard Hill Rd<br>Location 2 - 58 Millbrook Ct # 3<br>Dunmore, NH 03201
  </div>
  <div class="abs info" style="top:158px">
    <p class="lbl">Location:</p>
    <p><b>Began:</b>&nbsp; Friday, May 24, 2013 at 10:06 AM EDT</p>
    <p><b>Ends:</b>&nbsp; Wednesday, June 05, 2013 at 10:00 AM EDT</p>
    2270 Ashford Ln. NE<br>Concord, NH 03301
  </div>
</article>

<div class="abs video" role="img" aria-label="Video still of an auctioneer presenting a large gold coin"></div>
<svg class="abs" style="left:765px;top:522px" width="60" height="44" viewBox="0 0 60 44"><rect width="60" height="44" rx="4" fill="rgba(0,0,0,.55)"/><polygon points="23,10 23,34 42,22" fill="#fff"/></svg>
<div class="abs vbar">
  <svg class="abs" style="left:7px;top:6px" width="8" height="8"><polygon points="0,0 0,8 7,4" fill="#fff"/></svg>
  <span class="abs" style="left:28px;top:5px">00:00</span>
  <span class="abs" style="left:62px;top:8px;width:75px;height:4px;background:#444"></span>
  <span class="abs" style="left:146px;top:5px">00:00</span>
  <span class="abs" style="left:185px;top:6px;width:28px;height:8px;background:repeating-linear-gradient(90deg,#fff 0 1px,transparent 1px 3px)"></span>
  <svg class="abs" style="left:225px;top:5px" width="10" height="10"><path d="M0 3V0H3M7 0H10V3M10 7V10H7M3 10H0V7" fill="none" stroke="#fff" stroke-width="1.4"/></svg>
</div>

<section class="abs signup">
  <h2>Email sign up</h2>
  <div class="field">Enter Your Name</div>
  <div class="field">Enter Your Email Address...</div>
  <div class="subscribe">Subscribe</div>
</section>

<section class="abs testi">
  <h2>Client Testimonials</h2>
  <p><span class="q">&ldquo;</span>simply dummy text of the printing and typesetting industry. Lorem Ipsum has been the industry's took a galley of type and scrambledstandard dummy text ever since the 1500s, when an unknown printer took<span class="q">&rdquo;</span></p>
  <div class="by">By Helen Parks...</div>
</section>

<footer class="abs footer">
  <div class="contact"><b>Phone:</b> 603- 555-0188, <b>Email:</b> info@brookmereauction.com<br>Copyright (C) BROOKMERE 2013 - 2014 .&nbsp; All Rights Reserved</div>
  <div class="flogo"><i></i>BROOKMERE</div>
  <div class="badge1"></div>
  <div class="badge2"></div>
</footer>
</body>
</html>
```